HollowPine Ventures Inc. Business Card Design

My business is custom renovations and homes.I would need to have a new business logo created to go along with my company name. The business card should be of a modern style as this is the market I am focused on. I would need my contact information and website posted on the card. I would also like to list a few of the tasks I conduct on the card (such as: Renovations, Additions, Repairs, New Homes, Design, Consultations). On the reverse of the card I currently have just my logo and my motto, "Shaping A Bold Path". However, I am open to completely changing everything as I am starting a new year and would like to excel further. Any new ideas and suggestions are always welcomed. Thank you.

Target Market(s)

Upscale residential and commercial renovations and builds

Industry/Entity Type

Business

Contact Information for Business Card

I would like the design to be able to be laser cut or burnt onto a wooden business card. I will be creating one option of cards for really loyal customers (wooden) and a second option for the everyday customer (paper).

Font styles to use
Other font styles liked:
• Calibri / anything of mordern taste

Colors
f37122
5c5c5c
474747
ffffff

Requirements
Must have
• I would like the colours of my business to be a sharp orange and grey. I believe this will symbolize a modern style. I am open to other suggestions if this is not suitable for the designers tastes. My contact info as follows:
• Will Marsh
• President
• HollowPine Ventures Inc.
• 555-214-3987
• will@hollowpineventures.example
• I would like my website (currently under construction) hollowpineventures.example on the card aswell.
Nice to have
• Along with a modern logo representing HollowPine, I would like something on the card besides the logo and contact information. Perhaps a small background design. I feel it may be nice to have my services listed on the card (in smaller font on the bottom) Renovations, Additions, Repairs, Design, Consultations.
Should not have
• The business card should not have too many different colors. Should not have rounded corners.

```html
<!DOCTYPE html>
<html lang="en">
<head>
<meta charset="utf-8">
<title>HollowPine Ventures Inc. Business Card</title>
<link href="https://fonts.googleapis.com/css2?family=Roboto:ital,wght@0,400;0,500;0,700;1,700&family=Open+Sans:wght@400;600&family=Kaushan+Script&display=swap" rel="stylesheet">
<style>
  :root {
    --orange: #f37122;
    --grey-dark: #474747;
    --grey-mid: #5c5c5c;
    --white: #ffffff;
    --ink: #1e1e1e;
    --stage: #e9e6e1;
  }
  * { margin: 0; padding: 0; box-sizing: border-box; }
  html, body {
    width: 1200px; height: 800px; overflow: hidden;
    background: var(--stage);
  }
  .stage {
    position: relative; width: 1200px; height: 800px;
  }
  .card {
    position: absolute; top: 245px;
    width: 540px; height: 310px;
    box-shadow: 0 10px 28px rgba(0,0,0,0.18);
  }
  /* Back of card */
  .card-back {
    left: 40px; background: var(--grey-dark); color: var(--white);
  }
  .brand {
    display: flex; align-items: center; gap: 12px;
    font-family: "Roboto", sans-serif; font-weight: 500;
  }
  .brand-dot {
    width: 30px; height: 30px; border-radius: 50%;
  }
  .card-back .brand {
    position: absolute; top: 82px; left: 0; right: 0; justify-content: center;
    font-size: 44px; color: var(--white);
  }
  .card-back .brand-dot { background: var(--orange); }
  .motto {
    position: absolute; top: 160px; left: 0; right: 0; text-align: center;
    font-family: "Kaushan Script", cursive; font-size: 26px; color: var(--orange);
  }
  .services {
    position: absolute; bottom: 26px; left: 0; right: 0; text-align: center;
    font-family: "Open Sans", sans-serif; font-size: 12.5px; letter-spacing: 1.2px;
    text-transform: uppercase; color: var(--white);
  }
  /* Front of card */
  .card-front {
    left: 620px; background: var(--white); color: var(--ink);
  }
  .person {
    position: absolute; top: 34px; left: 36px;
    font-family: "Roboto", sans-serif;
  }
  .person-name {
    font-size: 22px; font-weight: 700; letter-spacing: 0.5px; text-transform: uppercase;
  }
  .person-title {
    font-size: 15px; font-weight: 700; font-style: italic; color: var(--orange);
    text-transform: uppercase; margin-top: 2px;
  }
  .contacts {
    position: absolute; top: 128px; left: 36px; list-style: none;
    font-family: "Roboto", sans-serif; font-size: 14px; font-weight: 500; line-height: 1.55;
  }
  .contacts .label { color: var(--orange); font-weight: 700; }
  .card-front .brand {
    position: absolute; right: 34px; bottom: 44px;
    font-size: 36px; color: var(--grey-dark);
  }
  .card-front .brand-dot { background: var(--orange); width: 26px; height: 26px; }
</style>
</head>
<body>
<main class="stage">
  <section class="card card-back" aria-label="Back of business card">
    <div class="brand"><span class="brand-dot"></span><span class="brand-name">HollowPine</span></div>
    <p class="motto">Shaping A Bold Path</p>
    <p class="services">Renovations | Additions | Repairs | New Homes | Design | Consultations</p>
  </section>

  <section class="card card-front" aria-label="Front of business card">
    <div class="person">
      <h1 class="person-name">Will Marsh</h1>
      <p class="person-title">President</p>
    </div>
    <ul class="contacts">
      <li><span class="label">P:</span> 555-214-3987</li>
      <li><span class="label">E:</span> will@hollowpineventures.example</li>
      <li><span class="label">W:</span> www.hollowpineventures.example</li>
    </ul>
    <div class="brand"><span class="brand-dot"></span><span class="brand-name">HollowPine</span></div>
  </section>
</main>
</body>
</html>
```